Poster Design - Stand Up Paddle Eco Tour

We need a A3 size poster design (using Adobe Illustrator) for our company's stand up paddle tour. Our tour is on flat water, calm and safe, suitable for all ages and level.

WE provide worldclass SUP boards for our customers. And branded Joren Maltby life jacket. Our instructors are all well trained and exeprience. Plus they are super friendly. Every paddling trip come with a safety boat.

Please refer to attached files for text and photos.

Our website is www.brinkwaveoar.com.sg

IMPORTANT NOTE - The design has to be done in Adobe Illustrator. The winning designer has to submit the working file in Adobe Illustrator.

Target Market(s)

Working adult - 20 - 35 year old

Industry/Entity Type

Tourism

Requirements
Must have
• The project MUST be done in Adobe Illustrator and the winning designer has to submit the artwork to us in Adobe Illustrator format.
Nice to have
• pleasant to look at.

```html
<!DOCTYPE html>
<html lang="en">
<head>
<meta charset="utf-8">
<title>Brinkwave Oar – SUP Eco Tour Poster</title>
<link rel="stylesheet" href="https://fonts.googleapis.com/css2?family=PT+Sans:ital,wght@0,400;0,700;1,700&family=PT+Sans+Narrow:wght@700&display=swap">
<style>
  :root{
    --navy:#13263f;
    --navy-deep:#0d1d33;
    --blue:#1e5c96;
    --blue-light:#3d7fbd;
    --paper:#ffffff;
    --mist:#e9eaec;
    --mist-dark:#c9cbce;
    --ink:#16233a;
    --white:#ffffff;
    --sky:#dfe9f1;
    --canopy:#2c5a2a;
    --canopy-light:#4c7a3c;
    --river:#6e6b4a;
    --river-deep:#4f4d36;
  }
  *{margin:0;padding:0;box-sizing:border-box}
  html,body{width:872px;height:1200px;overflow:hidden;background:var(--paper)}
  .poster{position:relative;width:872px;height:1200px;overflow:hidden;
    font-family:"PT Sans",Arial,sans-serif;color:var(--ink);background:var(--paper)}
  .hero-photo{position:absolute;left:0;top:95px;width:872px;height:590px;
    background:linear-gradient(180deg,var(--sky) 0%,var(--sky) 9%,var(--canopy-light) 12%,var(--canopy) 20%,#2a4f29 29%,#55603f 34%,var(--river) 46%,#67654a 66%,var(--river-deep) 100%)}
  .shapes{position:absolute;left:0;top:0}
  .headline{position:absolute;top:34px;left:0;width:872px;text-align:center;
    font-family:"PT Sans Narrow","PT Sans",sans-serif;font-weight:700;font-size:27px;line-height:39px;
    color:var(--navy);letter-spacing:.2px}
  .thumb{position:absolute;width:136px;height:136px;border-radius:50%;border:4px solid var(--navy);
    background:linear-gradient(180deg,#cfe2f2 0%,#e4eef6 38%,#9fb3a6 50%,#7c8b7c 70%,#6d7a6b 100%);
    box-shadow:0 2px 6px rgba(0,0,0,.35)}
  .pitch{position:absolute;left:30px;top:736px;width:690px}
  .pitch-title{font-family:"PT Sans Narrow","PT Sans",sans-serif;font-weight:700;font-size:23px;line-height:30px;color:var(--navy)}
  .pitch-lead{font-size:18px;line-height:26px;margin-top:3px;color:var(--ink)}
  .details{position:absolute;left:30px;top:896px;width:560px;font-size:15px;line-height:22px}
  .details .cta{font-weight:700;font-style:italic;font-size:18px;margin-top:2px}
  .schedule{margin-top:24px}
  .schedule b{font-weight:700}
  .brand{position:absolute;left:590px;top:970px;width:230px;
    font-weight:700;font-size:27px;color:var(--navy);display:flex;align-items:center;justify-content:center;gap:10px}
  .brand-dot{width:14px;height:14px;border-radius:50%;background:var(--navy);flex:none}
  .footer{position:absolute;left:40px;top:1100px;font-size:12.5px;line-height:16px;color:var(--white)}
  .footer .booking{margin-top:4px;font-size:13px}
  .footer .booking b{font-weight:700}
</style>
</head>
<body>
<main class="poster">
  <div class="hero-photo" role="img" aria-label="Photo of a group of stand up paddlers on a calm mangrove river, raising their paddles"></div>

  <svg class="shapes" width="872" height="1200" viewBox="0 0 872 1200" aria-hidden="true">
    <defs>
      <linearGradient id="mistFade" x1="0" y1="0" x2="0" y2="1">
        <stop offset="0" stop-color="#ffffff"/>
        <stop offset=".5" stop-color="#eceded"/>
        <stop offset="1" stop-color="#c8cacd"/>
      </linearGradient>
    </defs>
    <path d="M0 0H872V105C700 160 470 150 250 128C150 118 60 112 0 110Z" fill="var(--paper)"/>
    <path d="M250 128C470 150 700 160 872 105V140C700 185 470 170 250 128Z" fill="var(--blue)"/>
    <path d="M330 136C520 158 700 162 872 118V124C700 168 520 162 330 136Z" fill="var(--blue-light)" opacity=".6"/>
    <path d="M0 650C200 630 520 660 872 760V1200H0Z" fill="var(--navy)"/>
    <path d="M0 665C220 648 520 680 872 790V1200H0Z" fill="var(--blue)"/>
    <path d="M0 690C260 672 560 705 872 830V1200H0Z" fill="url(#mistFade)"/>
    <path d="M0 1068C250 1050 520 1060 872 1150V1200H0Z" fill="var(--blue)"/>
    <path d="M0 1078C250 1062 520 1072 872 1165V1200H0Z" fill="var(--navy-deep)"/>
  </svg>

  <h1 class="headline">EXPLORE THE NATURAL COASTAL SURROUNDINGS AND WATERWAYS<br>OF JOHOR ON A SUP ADVENTURE TOURING BOARD</h1>

  <div class="thumb" role="img" aria-label="Paddlers on open water" style="left:365px;top:611px"></div>
  <div class="thumb" role="img" aria-label="Paddler beside the mangroves" style="left:530px;top:637px"></div>
  <div class="thumb" role="img" aria-label="Group of paddle boards lined up" style="left:701px;top:678px"></div>

  <section class="pitch">
    <h2 class="pitch-title">WHAT COULD BE BETTER<br>THAN A GROUP GUIDED TOUR?</h2>
    <p class="pitch-lead">With life vests and a safety boat for our guided tour, you can be assured of a secured environment while you focus on just having fun and creating life’s best memories with friends and family.</p>
  </section>

  <section class="details">
    <p>Our tours are flat-water and appropriate for all ages and levels.<br>We have the best possible service and equipment.</p>
    <p class="cta">Join us for a fun and relaxing day.</p>
    <p class="schedule"><b>TIMING</b>: Morning, afternoon, and sunset session<br><b>LOCATION:</b> Tanjung Reed River, set off from Teluk Seri,<br>Kuala Damai. (next to Batu Hijau)</p>
  </section>

  <div class="brand"><span class="brand-dot"></span><span>Brinkwave Oar</span></div>

  <footer class="footer">
    <p>Contact us for booking.<br>We do not accept walk-in.<br><b>www.brinkwaveoar.com.sg</b><br>Facebook: Brinkwave Oar</p>
    <p class="booking">Booking Contact: <b>booking@brinkwaveoar.com.sg</b></p>
  </footer>
</main>
</body>
</html>
```